Professional Learning Organization for Educators needs a Design Thinking Workshop Flyer

We need a flyer for a series of Introductory Design Thinking workshops we're delivering for education leaders.

We have generated our own version of the flyer with a word template, but want it to look even more professional and eye catching. It is attached.

We had an image that we thought might be good, but pulled it out so we don't bias designers' thinking.
Updates

Reason: We are a bit flexible on the deadline since this is a holiday week and people are traveling

Target Market(s)

Very busy education leaders whose curiosity needs to be stimulated enough to enroll in the course

Industry/Entity Type

Education

Font styles to use
Other font styles liked:
• Century Gothic or something closer to that

Requirements
Must have
• Some version of the text that is on the current flyer that I attached.
Nice to have
• I am very flexible and open right now on this design.

```html
<!DOCTYPE html>
<html lang="en">
<head>
<meta charset="utf-8">
<title>Design Thinking Workshops</title>
<link href="https://fonts.googleapis.com/css2?family=Bodoni+Moda:wght@400&family=Didact+Gothic&family=Montserrat:wght@700&display=swap" rel="stylesheet">
<style>
  :root{
    --gold:#dcbf2f;
    --blue:#0a84c6;
    --ink:#2b2b2b;
    --white:#ffffff;
    --rule:#5a5020;
  }
  *{margin:0;padding:0;box-sizing:border-box}
  html,body{width:849px;height:1200px;overflow:hidden;background:var(--blue)}
  .flyer{position:relative;width:849px;height:1200px;background:var(--blue);font-family:"Didact Gothic","Century Gothic",sans-serif;color:var(--white)}
  .hero{position:absolute;left:0;top:0;width:849px;height:390px;background:var(--gold)}
  .hero-rule{position:absolute;left:408px;top:50px;width:441px;height:1px;background:var(--white)}
  .hero-art{position:absolute;left:432px;top:55px;width:417px;height:335px;border-radius:46% 0 0 30% / 40% 0 0 20%;
    background:radial-gradient(ellipse at 60% 45%, #111 0%, #1c1c1c 55%, #2e2a16 85%, #5a5020 100%)}
  .title{position:absolute;left:0;top:0;width:460px;height:290px;font-family:"Bodoni Moda",serif;font-weight:400;color:var(--white);line-height:1}
  .title span{position:absolute;left:60px;white-space:nowrap}
  .title .t1{top:60px;font-size:99px}
  .title .t2{top:149px;font-size:72px}
  .title .t3{top:223px;font-size:59px}
  .tagline{position:absolute;left:64px;top:289px;width:378px;border-top:2px solid var(--rule);border-bottom:2px solid var(--rule);padding:5px 0 3px;font-size:16px;letter-spacing:1.1px;color:var(--ink);white-space:nowrap}
  .intro{position:absolute;left:64px;top:405px;width:724px;font-size:17px;line-height:21px;letter-spacing:.45px;text-align:justify}
  .points{position:absolute;left:76px;top:493px;width:715px;list-style:none;font-size:17px;line-height:21px;letter-spacing:.45px}
  .points li{position:relative;padding-left:46px;margin-bottom:10px}
  .points svg{position:absolute;left:0;top:2px}
  .schedule{position:absolute;left:57px;top:671px;width:723px;height:146px;display:grid;grid-template-columns:361px 362px;grid-template-rows:73px 73px;color:var(--ink);text-align:center}
  .slot{display:flex;flex-direction:column;justify-content:center;align-items:center}
  .slot.light{background:var(--white)}
  .slot.gold{background:var(--gold)}
  .slot .day{font-size:19px;letter-spacing:.4px}
  .slot .dates{font-family:"Montserrat",sans-serif;font-weight:700;font-size:17px;margin-top:2px}
  .slot.small .day{font-size:15px;letter-spacing:.3px}
  .slot.small .dates{font-size:14px}
  .voices{position:absolute;left:0;top:0;width:849px;height:1005px;text-align:center}
  .voices h2{position:absolute;left:0;top:820px;width:849px;font-family:"Montserrat",sans-serif;font-weight:700;font-size:14px;color:var(--gold)}
  .quote{position:absolute;left:0;width:849px;font-size:17px;line-height:21px;letter-spacing:.4px}
  .q1{top:848px}.q2{top:905px}.q3{top:960px}
  .divider{position:absolute;left:115px;width:618px;border-top:1px dotted var(--gold)}
  .d1{top:899px}.d2{top:953px}
  .links{position:absolute;left:0;top:1004px;width:849px;text-align:center;font-family:"Montserrat",sans-serif;font-weight:700;font-size:21px;line-height:28px}
  .links .site{color:var(--gold)}
  .enroll{position:absolute;left:62px;top:1063px;width:718px;height:82px;background:var(--gold);color:var(--ink);text-align:center;padding-top:13px;font-size:15px;line-height:19px;letter-spacing:.3px}
  .enroll strong{font-family:"Montserrat",sans-serif;font-weight:700;font-size:14px;letter-spacing:0}
</style>
</head>
<body>
<div class="flyer">
  <header class="hero">
    <div class="hero-rule"></div>
    <div class="hero-art" role="img" aria-label="Dark head silhouette in profile filled with small floating outline shapes"></div>
    <h1 class="title"><span class="t1">DESIGN</span><span class="t2">THINKING</span><span class="t3">WORKSHOPS</span></h1>
    <p class="tagline">DESIGNING YOUR WAY TO BETTER SOLUTIONS.</p>
  </header>

  <p class="intro">Maplecrest Public Schools and Ridgeline BOCES invite you to discover the power of Design Thinking.&nbsp; During our three session course, you will learn and practice mind sets and tools that help you continuously and creatively improve the experiences of the people you serve by:</p>

  <ul class="points">
    <li><svg width="30" height="26" viewBox="0 0 30 26"><g fill="#e8c23a"><circle cx="10" cy="10" r="7"/><circle cx="18" cy="8" r="7"/><circle cx="22" cy="14" r="5"/><circle cx="13" cy="15" r="6"/><circle cx="5" cy="22" r="1.6"/><circle cx="2" cy="25" r="1"/></g></svg>Understanding what your teachers, students and community truly need in their<br>learning and work experiences</li>
    <li><svg width="30" height="26" viewBox="0 0 30 26"><g fill="#e8c23a"><circle cx="10" cy="10" r="7"/><circle cx="18" cy="8" r="7"/><circle cx="22" cy="14" r="5"/><circle cx="13" cy="15" r="6"/><circle cx="5" cy="22" r="1.6"/><circle cx="2" cy="25" r="1"/></g></svg>Designing solutions that better meet their needs<br>Seeking authentic feedback and reactions to these solutions prior to their<br>implementation.</li>
    <li><svg width="30" height="26" viewBox="0 0 30 26"><g fill="#e8c23a"><circle cx="10" cy="10" r="7"/><circle cx="18" cy="8" r="7"/><circle cx="22" cy="14" r="5"/><circle cx="13" cy="15" r="6"/><circle cx="5" cy="22" r="1.6"/><circle cx="2" cy="25" r="1"/></g></svg>We are offering this three-session course at four different times in spring semester.<br>Please choose the course that works best for your schedule.</li>
  </ul>

  <section class="schedule">
    <div class="slot light"><span class="day">MONDAY MORNINGS</span><span class="dates">1/23, 1/30 AND 2/6</span></div>
    <div class="slot gold small"><span class="day">TUESDAY AFTERNOONS</span><span class="dates">2/7, 2/14 AND 2/21</span></div>
    <div class="slot gold small"><span class="day">WEDNESDAY AFTERNOONS</span><span class="dates">3/8, 3/15 AND 3/22</span></div>
    <div class="slot light"><span class="day">WEDNESDAY EVENINGS</span><span class="dates">2/8, 2/15 AND 2/22</span></div>
  </section>

  <section class="voices">
    <h2>WHAT OUR PARTICIPANTS SAY…</h2>
    <p class="quote q1">“This has been an empowering experience that allowed me to try<br>out dramatic changes in my practice that I wouldn't have imagined before.”</p>
    <div class="divider d1"></div>
    <p class="quote q2">“I never realized how often I've guessed and assumed what our<br>teachers and students need – now I have a way to stop guessing!”</p>
    <div class="divider d2"></div>
    <p class="quote q3">“I finally have tools to generate truly creative ideas that people actually<br>embrace… because they meet their needs”</p>
  </section>

  <div class="links">
    <div class="site">RIDGELINE BOCES WWW.RIDGELINEBOCES.ORG</div>
    <div class="contact">QUESTIONS? INFO@RIDGELINELEARN.ORG</div>
  </div>

  <footer class="enroll">
    <strong>CLICK HERE TO ENROLL. GO TO WWW.RIDGELINEBOCES.ORG TO LEARN MORE.</strong><br>
    This course is held in Maplecrest Public Schools.<br>
    No fee for MPS leaders. $150 fee for leaders outside of MPS.
  </footer>
</div>
</body>
</html>
```